Labelling for Ice cream products for Tindle k's company

Hi
We are an Ice cream/Gelato company based in Birmingham UK. We need a design for packaging for some of our products. We are in need of packaging for round 400-500ml tubs and smaller round 125ml tubs (with lids). We also need a design for our plastic Ice Lolly wrappers (will provide dimensions if needed) this will be for a roll that is used on an Ice lolly wrapping machine, and also designs for stickers that will go on the top of 10 litre tubs and rectangular stickers for the side of 5 litre napoli pans. We currently have a diner that we sell, so a simple design for our inhouse scoop cups would also be good. The designs should be editable and allow for incorporation of pictures of different flavours. I will attach our logo, as we would like the design to be congruent with the logos colours. The design farrow quills currently use is nice and though we want our packaging to be unique, something along those lines is were our minds are at t he moment. The designer is free to play with designs and make it look as high quality as they wish, though is must preferably look fun but not childish. A design that incorporates pascal colours would be nice but not essential so feel free to experiment.
So to conclude:
1. Design for 400-500ml round tubs with lids.
2. Design for Ice lolly wrappers.
3. Design for square labels for the top of 10 litre tubs and rectangular labes for the side of 5 litre napoli pans.
4. Basic design for in-house scoop cups.
I will upload our logo.
Many thanks and kind regards

Derek

• It would also be nice to have a design for spindora wrappers

```html
<!DOCTYPE html>
<html lang="en">
<head>
<meta charset="utf-8">
<title>Strawberry Ice Cream – Tub Label</title>
<link href="https://fonts.googleapis.com/css2?family=Montserrat:wght@300;800&display=swap" rel="stylesheet">
<style>
  :root {
    --canvas: #ffffff;
    --label-pink: #f8d3dc;
    --label-pink-light: #fbdde4;
    --berry: #c8174a;
    --berry-deep: #a80d34;
    --cone-pink: #d4336a;
    --cone-dark: #3b3436;
    --scoop-red: #e2405c;
    --scoop-cream: #efe2cf;
  }
  html, body {
    margin: 0;
    padding: 0;
    width: 1200px;
    height: 1200px;
    overflow: hidden;
    background: var(--canvas);
  }
  .tub-label {
    position: absolute;
    left: 120px;
    top: 156px;
    width: 960px;
    height: 888px;
    display: block;
  }
  .flavour-outline {
    font-family: "Montserrat", sans-serif;
    font-weight: 300;
    fill: none;
    stroke: var(--berry);
    stroke-width: 2.4;
    letter-spacing: 2px;
  }
  .product-name {
    font-family: "Montserrat", sans-serif;
    font-weight: 800;
    fill: var(--berry);
  }
</style>
</head>
<body>
<svg class="tub-label" viewBox="0 0 960 888" xmlns="http://www.w3.org/2000/svg">
  <defs>
    <linearGradient id="label-bg" x1="0" y1="0" x2="1" y2="0">
      <stop offset="0" stop-color="var(--label-pink)"/>
      <stop offset="0.55" stop-color="var(--label-pink-light)"/>
      <stop offset="1" stop-color="var(--label-pink)"/>
    </linearGradient>
    <linearGradient id="cone-red-dark" x1="0" y1="0" x2="0" y2="1">
      <stop offset="0" stop-color="var(--scoop-red)"/>
      <stop offset="0.35" stop-color="var(--scoop-red)"/>
      <stop offset="0.45" stop-color="var(--cone-dark)"/>
      <stop offset="1" stop-color="var(--cone-dark)"/>
    </linearGradient>
    <linearGradient id="cone-cream-pink" x1="0" y1="0" x2="0" y2="1">
      <stop offset="0" stop-color="var(--scoop-cream)"/>
      <stop offset="0.38" stop-color="var(--scoop-cream)"/>
      <stop offset="0.48" stop-color="var(--cone-pink)"/>
      <stop offset="1" stop-color="var(--cone-pink)"/>
    </linearGradient>
    <clipPath id="label-area">
      <rect width="960" height="888"/>
    </clipPath>
  </defs>

  <rect class="label-background" width="960" height="888" fill="url(#label-bg)"/>

  <g class="flavour-photos" clip-path="url(#label-area)">
    <rect role="img" aria-label="Strawberry scoop in a dark waffle cone" x="40" y="30" width="130" height="456" rx="40" fill="url(#cone-red-dark)" transform="rotate(-8 105 258)"/>
    <rect role="img" aria-label="Empty pink waffle cone, point down" x="230" y="-20" width="160" height="320" rx="50" fill="var(--cone-pink)" transform="rotate(6 310 140)"/>
    <rect role="img" aria-label="Empty dark waffle cone, point down" x="520" y="-20" width="80" height="146" rx="30" fill="var(--cone-dark)"/>
    <rect role="img" aria-label="Strawberry scoop in a dark waffle cone" x="712" y="432" width="140" height="436" rx="44" fill="url(#cone-red-dark)" transform="rotate(4 782 650)"/>
    <rect role="img" aria-label="Vanilla scoop in a pink waffle cone" x="500" y="618" width="160" height="300" rx="50" fill="url(#cone-cream-pink)"/>
    <rect role="img" aria-label="Strawberry scoop at the lower edge" x="282" y="826" width="160" height="90" rx="40" fill="var(--scoop-red)"/>
    <rect role="img" aria-label="Vanilla scoop in a pink cone at the right edge" x="890" y="234" width="70" height="432" rx="30" fill="url(#cone-cream-pink)"/>
    <rect role="img" aria-label="Vanilla scoop in a pink cone at the left edge" x="-30" y="246" width="64" height="360" rx="28" fill="url(#cone-cream-pink)"/>
  </g>

  <g class="title-block">
    <text class="flavour-outline" x="80" y="760" font-size="138" textLength="1010" lengthAdjust="spacingAndGlyphs" transform="rotate(-43 80 760)">STRAWBERRY</text>
    <text class="product-name" x="285" y="728" font-size="92" textLength="560" lengthAdjust="spacingAndGlyphs" transform="rotate(-42 285 728)">ICE CREAM</text>
  </g>
</svg>
</body>
</html>
```